Business Card Design Project

We are an incubator company that helps young entrepreneur to launch new ideas into the market. We will be targeting investors or likewise; Angels, young entrepreneurs and technopreneurs.

Our logo is being tasked by artflockly to design, therefore there is no logo for now.
You can us Lanternfold Pte Ltd as the logo for the time being.

Please let us have some versions of modern and yet professional designs; for words, you can indicate e.g (address), (Title)

thanks

Target Market(s)

young entrepreneurs
angels, investors

Industry/Entity Type

Business

Colors
3176b5
ffffff

Requirements
Must have
• able to project out our name; Lanternfold
Should not have
• Nothing childish or cartoon

```html
<!DOCTYPE html>
<html lang="en">
<head>
<meta charset="utf-8">
<title>Lanternfold Business Card</title>
<link rel="stylesheet" href="https://fonts.googleapis.com/css2?family=Open+Sans:wght@400;600;700&display=swap">
<style>
  :root {
    --brand-blue: #3176b5;
    --card-light: #6aa9de;
    --card-mid: #3a7cc4;
    --card-deep: #1c4f9c;
    --logo-navy: #1a4a8e;
    --white: #ffffff;
    --page-bg: #e9edf1;
  }
  * { margin: 0; padding: 0; box-sizing: border-box; }
  html, body {
    width: 1200px; height: 900px; overflow: hidden;
    background: var(--page-bg);
    font-family: "Open Sans", Arial, sans-serif;
  }
  .canvas {
    position: relative; width: 1200px; height: 900px;
    display: flex; align-items: center; justify-content: center; gap: 50px;
  }
  .card {
    position: relative; width: 525px; height: 300px;
    border-radius: 18px; overflow: hidden;
    background: linear-gradient(170deg, var(--card-light) 0%, var(--card-mid) 50%, var(--card-deep) 100%);
    box-shadow: 0 10px 24px rgba(20, 50, 90, 0.25);
    color: var(--white);
  }
  .card__gloss {
    position: absolute; inset: 0; z-index: 0;
    background: linear-gradient(160deg, transparent 38%, rgba(255,255,255,0.3) 45%, transparent 52%);
    pointer-events: none;
  }
  .brand, .identity, .contacts { z-index: 1; }
  .brand { display: flex; flex-direction: column; align-items: flex-start; }
  .brand__row { display: flex; align-items: center; gap: 10px; }
  .brand__mark { width: 34px; height: 34px; background: var(--logo-navy); border-radius: 4px; }
  .brand__name {
    font-weight: 700; font-variant: small-caps; letter-spacing: 1px;
    color: var(--logo-navy); font-size: 30px; line-height: 1;
  }
  .brand__tagline {
    font-weight: 700; font-variant: small-caps; font-size: 11px; letter-spacing: 2px;
    color: var(--logo-navy); margin-top: 4px; padding-left: 44px;
  }
  .card--front .brand {
    position: absolute; left: 50%; top: 50%; transform: translate(-50%, -50%);
  }
  .card--back .brand { position: absolute; left: 26px; top: 24px; }
  .card--back .brand__name { font-size: 22px; }
  .card--back .brand__mark { width: 26px; height: 26px; }
  .card--back .brand__tagline { font-size: 9px; padding-left: 36px; }
  .identity {
    position: absolute; right: 26px; top: 20px; text-align: right;
    font-variant: small-caps; letter-spacing: 2px; line-height: 1.1;
  }
  .identity__name { font-size: 21px; font-weight: 600; }
  .identity__title { font-size: 19px; }
  .identity__address { font-size: 15px; margin-top: 4px; }
  .contacts {
    position: absolute; left: 26px; right: 26px; bottom: 20px;
    display: flex; flex-direction: column; gap: 10px;
  }
  .contact {
    display: flex; align-items: center; height: 24px;
    border: 1px solid rgba(255,255,255,0.85);
  }
  .contact__bar { width: 90px; height: 6px; background: var(--white); margin: 0 16px 0 10px; }
  .contact__text { font-size: 13px; letter-spacing: 2px; }
  .contact__end { margin-left: auto; width: 70px; height: 6px; background: var(--white); margin-right: 10px; }
</style>
</head>
<body>
<main class="canvas">
  <section class="card card--front" aria-label="Card front">
    <div class="card__gloss"></div>
    <div class="brand">
      <div class="brand__row">
        <span class="brand__mark"></span>
        <span class="brand__name">Lanternfold</span>
      </div>
      <span class="brand__tagline">Launching Bold Ventures</span>
    </div>
  </section>

  <section class="card card--back" aria-label="Card back">
    <div class="card__gloss"></div>
    <div class="brand">
      <div class="brand__row">
        <span class="brand__mark"></span>
        <span class="brand__name">Lanternfold</span>
      </div>
      <span class="brand__tagline">Launching Bold Ventures</span>
    </div>
    <div class="identity">
      <div class="identity__name">Name Surname</div>
      <div class="identity__title">Designation</div>
      <div class="identity__address">Address<br>Lane 1<br>Street 1<br>City<br>State</div>
    </div>
    <div class="contacts">
      <div class="contact"><span class="contact__bar"></span><span class="contact__text">+12345678910</span><span class="contact__end"></span></div>
      <div class="contact"><span class="contact__bar"></span><span class="contact__text">email@lanternfold.com</span><span class="contact__end"></span></div>
      <div class="contact"><span class="contact__bar"></span><span class="contact__text">www.lanternfold.com</span><span class="contact__end"></span></div>
    </div>
  </section>
</main>
</body>
</html>
```